International Manufacturing Business Needs A Heavy Hitting Wordpress Design!

We need wordpress template designs for a new website for our UK based International company Tolvane Engineering Ltd. We manufacture and supply steel security doors and window units. We would like designs that feature the black and yellow industrial "stripes" that can be seen at our current site www.tolvadoors.com. The final design should communicate strength, power and weight to represent the quality of the products and the security that they provide.

It feels like we need 3 different types of page to be able to be created as per the current website at www.tolvasecuredoors.com.

Homepage
Products/Accessories
Leadtimes/Downloads/Contact

It may be that 3 different page types can be created with one template. I'm totally open to this.

I don't like the way that the site currently handles product images, nobody wants to click on even thumbnail to see the product. http://tolvasecuredoors.com/products/personnel-doors/

Totally open to suggestions on layout to enable the feeling outlined in the brief above.

Please ask if anything is not clear or you need answers to drill down on specifics.

Sick

Target Market(s)

Businesses that buy steel doors

Font styles to use
Sans Serif
Other font styles liked:
• Copperplate Gothic Bold - For Company Name but we are open to suggestions

Colors

Designer to choose colors to be used in the design.

Requirements
Must have
• Professional looking, clean design
• Conveys strength, power and weight to represent the quality of the products, the characteristics of steel and the security that they provide.
• Incorporates black and yellow stripes of our branding
• Ability to create pages with content as seen at www.tolvasecuredoors.com
• A better way of showing the product images
Nice to have
• If possible. a design that gives off the feeling that not only do we supply the products we also make them in house too. I don't know what this looks like but a way of differentiating between a supply only business and one that manufacturers the product too.
Should not have
• We don't like the current thumbnail method of showing the product images

```html
<!DOCTYPE html>
<html lang="en">
<head>
<meta charset="utf-8">
<title>Tolvane Engineering Ltd – Steel Security Doors</title>
<link href="https://fonts.googleapis.com/css2?family=Cinzel:wght@400;700&family=Open+Sans:ital,wght@0,400;0,600;0,700;1,400&display=swap" rel="stylesheet">
<style>
:root{
  --teal:#4d8789;
  --teal-light:#7fb0b1;
  --teal-deep:#174d5e;
  --navy:#0e3d4f;
  --yellow:#f3d700;
  --ink:#2b2b2b;
  --grey:#666;
  --line:#d9dfe0;
  --white:#fff;
}
*{box-sizing:border-box;margin:0;padding:0}
html,body{width:1200px;height:3550px;overflow:hidden;background:var(--white)}
body{position:relative;font-family:"Open Sans",Arial,sans-serif;color:var(--ink);font-size:13px}
.heading{font-family:"Cinzel",Georgia,serif;font-weight:700;letter-spacing:1px}
.abs{position:absolute}

/* header */
.site-header{position:absolute;left:0;top:0;width:1200px;height:90px;background:var(--white);z-index:5}
.brand{position:absolute;left:140px;top:14px;display:flex;align-items:center;gap:12px}
.brand-square{width:34px;height:52px;background:var(--teal)}
.brand-name{font-family:"Cinzel",Georgia,serif;font-size:17px;line-height:20px;color:var(--teal);font-weight:400}
.top-contact{position:absolute;right:140px;top:18px;display:flex;gap:34px;font-size:12px;color:var(--teal);font-family:"Cinzel",serif}
.top-contact span{display:flex;align-items:center;gap:8px}
.main-nav{position:absolute;right:140px;top:66px;display:flex;gap:26px;font-family:"Cinzel",serif;font-size:12px;color:var(--teal)}
.main-nav .active{color:var(--ink);font-weight:700}

/* hero */
.hero{position:absolute;left:0;top:90px;width:1200px;height:545px;
  background:linear-gradient(160deg,#9fb9bb 0%,#6f9c9f 40%,#4f7f83 75%,#3d6d72 100%);
  clip-path:polygon(0 0,100% 0,100% 82%,0 100%)}
.hero-title{position:absolute;left:0;width:1200px;top:232px;text-align:center;color:var(--white);font-size:40px;line-height:52px;font-weight:400}
.scroll-cue{position:absolute;left:570px;top:465px;width:60px;text-align:center;color:var(--yellow);font-size:9px}

/* about */
.hex{position:absolute;width:166px;height:188px;clip-path:polygon(50% 0,100% 25%,100% 75%,50% 100%,0 75%,0 25%);background:var(--teal-light)}
.hex-inner{position:absolute;inset:4px;clip-path:polygon(50% 0,100% 25%,100% 75%,50% 100%,0 75%,0 25%);background:var(--white);display:flex;flex-direction:column;align-items:center;justify-content:center;gap:14px;color:var(--teal);font-size:13px;font-weight:600}
.about-title{position:absolute;left:585px;top:695px;font-size:34px;color:var(--ink)}
.about-rule,.section-rule{height:3px;background:var(--teal);width:100px}
.about-text{position:absolute;left:585px;top:765px;width:460px;font-size:12px;line-height:18px;color:var(--grey)}
.about-text p{margin-bottom:9px}
.btn{display:inline-block;background:var(--teal);color:var(--white);font-size:12px;padding:10px 20px;text-transform:uppercase}

/* products */
.products-bg{position:absolute;left:0;top:1010px;width:1200px;height:650px;
  background:linear-gradient(120deg,#5f9496 0%,#4a8285 50%,#3e7276 100%);
  clip-path:polygon(0 13%,100% 0,100% 100%,0 100%)}
.section-title{position:absolute;left:0;width:1200px;text-align:center;font-size:32px}
.products-copy{position:absolute;left:168px;top:1225px;width:400px;color:#e6f0f0;font-size:12px;line-height:18px}
.products-copy h3{font-family:"Cinzel",serif;font-size:20px;color:var(--white);font-weight:400;margin-bottom:10px}
.products-copy ul{margin:10px 0 12px 18px}
.products-copy a{color:var(--yellow);font-family:"Cinzel",serif;font-size:14px;text-decoration:underline}
.product-frame{position:absolute;left:648px;top:1230px;width:346px;height:235px;border:6px solid var(--yellow);background:linear-gradient(135deg,#d8d6cf,#b7b4aa 55%,#3b4a6a)}
.dots{position:absolute;left:572px;top:1498px;display:flex;gap:10px}
.dots i{width:8px;height:8px;border-radius:50%;border:1px solid #cfe0e0;display:block}
.dots i.on{background:#cfe0e0}

/* contact band */
.contact-band{position:absolute;left:0;top:1490px;width:1200px;height:415px;background:linear-gradient(90deg,#0d3447 0%,var(--navy) 45%,#123f52 100%);clip-path:polygon(0 15%,100% 0,100% 86%,0 100%)}
.contact-photo{position:absolute;left:0;top:1560px;width:330px;height:345px;background:radial-gradient(ellipse at 55% 45%,#5c7c88 0%,#1f4a5c 55%,transparent 75%);clip-path:polygon(0 0,100% 0,100% 85%,0 100%)}
.contact-title{top:1690px;color:var(--white);font-weight:400}
.contact-lead{position:absolute;left:360px;width:480px;top:1745px;text-align:center;color:#d7e4e8;font-size:12px;line-height:18px}
.contact-actions{position:absolute;left:0;width:1200px;top:1795px;display:flex;justify-content:center;align-items:center;gap:14px;color:var(--white);font-size:12px}
.ghost{border:1px solid #cfdde2;padding:8px 12px;color:var(--white);display:flex;align-items:center;gap:6px}
.or{color:var(--yellow);font-weight:700}

/* reviews */
.reviews-title{top:1900px;color:var(--ink)}
.avatar{position:absolute;clip-path:polygon(50% 0,100% 25%,100% 75%,50% 100%,0 75%,0 25%);background:linear-gradient(160deg,#d9c2a8,#8a7362)}
.arrow-btn{position:absolute;width:22px;height:22px;border-radius:50%;display:flex;align-items:center;justify-content:center}
.quote{position:absolute;left:270px;width:660px;top:2098px;text-align:center;font-style:italic;font-size:13px;line-height:22px;color:#555}
.quote-mark{position:absolute;left:588px;top:2178px;width:24px;height:24px;border-radius:50%;background:var(--teal);color:var(--white);text-align:center;font-family:Georgia,serif;font-size:20px;line-height:28px}
.reviewer{position:absolute;left:0;width:1200px;top:2212px;text-align:center;font-size:17px;color:#333}

/* latest */
.latest-bg{position:absolute;left:0;top:2235px;width:1200px;height:640px;background:linear-gradient(160deg,#7ea7ab 0%,#4d7a80 40%,#24495a 100%);clip-path:polygon(0 0,100% 9%,100% 100%,0 92%)}
.latest-title{top:2368px;color:var(--ink)}
.latest-card{position:absolute;left:268px;top:2455px;width:662px;height:340px;background:var(--white);box-shadow:0 6px 18px rgba(0,0,0,.25)}
.latest-copy{position:absolute;left:16px;top:18px;width:300px;font-size:12px;line-height:18px;color:#444}
.latest-copy h3{font-family:"Cinzel",serif;font-size:20px;font-weight:700;color:var(--ink);margin-bottom:12px}
.latest-copy p{margin-bottom:10px}
.latest-copy strong{color:var(--ink)}
.latest-image{position:absolute;left:330px;top:0;width:332px;height:340px;background:linear-gradient(120deg,#3d4248 0%,#5a6168 55%,#8d949a 100%)}

/* downloads */
.downloads-title{top:2878px;color:var(--ink)}
.brochure{position:absolute;top:2974px;height:106px;border:1px solid var(--line);border-radius:3px;text-align:center;font-size:12px;line-height:17px;color:#444;padding-top:14px}
.brochure svg{display:block;margin:0 auto 10px}

/* footer */
.footer-bg{position:absolute;left:0;top:3095px;width:1200px;height:455px;background:linear-gradient(180deg,#6e9ea3 0%,#3f7479 45%,#1e4b56 100%);clip-path:polygon(0 17%,100% 0,100% 100%,0 100%)}
.footer-actions{position:absolute;left:700px;top:3188px;display:flex;gap:14px;align-items:center;font-size:12px;color:var(--white)}
.footer-col{position:absolute;top:3255px;color:var(--white);font-size:11px}
.footer-col h4{font-family:"Cinzel",serif;font-weight:400;font-size:14px;margin-bottom:6px}
.footer-col .bar{width:60px;height:2px;background:var(--yellow);margin-bottom:14px}
.footer-col li{list-style:none;line-height:24px;font-weight:600}
.footer-col .address{line-height:16px;font-weight:600;display:flex;gap:10px;margin-bottom:14px}
.display-stand{position:absolute;left:700px;top:3275px;width:90px;height:170px;background:linear-gradient(90deg,#0f2d35,#4e8d8a 50%,#15353e);clip-path:polygon(0 8%,100% 0,100% 100%,0 92%)}
.field{width:225px;height:30px;background:var(--white);color:#888;font-size:11px;padding:8px 10px;margin-bottom:6px}
.submit{display:inline-block;background:var(--yellow);color:var(--ink);font-weight:700;font-size:12px;padding:8px 16px}
.copyright{position:absolute;left:143px;top:3516px;color:#dbe8ea;font-size:11px}
.socials{position:absolute;left:928px;top:3505px;display:flex;gap:6px}
.socials i{display:block;width:28px;height:28px;border-radius:50%;border:2px solid var(--white)}
</style>
</head>
<body>

<header class="site-header">
  <div class="brand"><div class="brand-square"></div><div class="brand-name">Tolvane<br>Engineering Ltd.</div></div>
  <div class="top-contact">
    <span><svg width="14" height="10" viewBox="0 0 14 10"><rect width="14" height="10" fill="#4d8789"/><path d="M0 0 7 6 14 0" stroke="#fff" fill="none"/></svg>SALES@TOLVADOORS.COM</span>
    <span><svg width="14" height="14" viewBox="0 0 14 14"><circle cx="7" cy="7" r="6.3" fill="none" stroke="#4d8789"/><path d="M4.5 4c1 3 2.5 4.5 5 5.5l.8-1.3-1.6-.9-.7.6C7 7.4 6.5 6.8 6 5.8l.6-.7-.9-1.6z" fill="#4d8789"/></svg>+44 (0)1632 960 300</span>
  </div>
  <nav class="main-nav"><span class="active">HOME</span><span>PRODUCTS &amp; ACCESSORIES</span><span>DELIVERY &amp; LEAD TIMES</span><span>DOWNLOADS</span><span>CONTACT</span></nav>
</header>

<section class="hero" role="img" aria-label="Photograph of a factory bay lined with steel security doors"></section>
<h1 class="hero-title heading">We manufacture &amp; supply steel<br>security doors &amp; window<br>units</h1>
<div class="scroll-cue"><svg width="16" height="10" viewBox="0 0 16 10"><path d="M1 1l7 7 7-7" stroke="#fff" stroke-width="2.5" fill="none"/></svg><br>SCROLL</div>

<div class="hex" style="left:289px;top:622px"><div class="hex-inner">
  <svg width="36" height="46" viewBox="0 0 36 46"><rect x="4" y="2" width="28" height="42" fill="none" stroke="#4d8789" stroke-width="3"/><rect x="9" y="6" width="18" height="38" fill="#4d8789"/><circle cx="23" cy="25" r="1.8" fill="#fff"/></svg>Personal Doors</div></div>
<div class="hex" style="left:208px;top:760px"><div class="hex-inner">
  <svg width="40" height="44" viewBox="0 0 40 44"><rect x="16" y="2" width="20" height="40" fill="none" stroke="#4d8789" stroke-width="3"/><path d="M2 22h20M15 15l7 7-7 7" stroke="#4d8789" stroke-width="3" fill="none"/></svg>Fire Exit Doors</div></div>
<div class="hex" style="left:370px;top:760px"><div class="hex-inner">
  <svg width="36" height="46" viewBox="0 0 36 46"><rect x="4" y="2" width="28" height="42" fill="none" stroke="#4d8789" stroke-width="3"/><path d="M9 6l16 5v33H9z" fill="#4d8789"/></svg>Blank Doors</div></div>

<h2 class="about-title heading">About Us</h2>
<div class="about-rule abs" style="left:585px;top:743px"></div>
<div class="about-text">
  <p>Tolvane security doors combine a high level of security with exceptional value.</p>
  <p>Our superior quality and proven reliability has made us the first choice for a wide range of companies no matter what their requirement or application.</p>
  <p>All of our products are designed and manufactured to the highest specification, combine this with a rigorous quality control system and an extensive after-sales service and it is easy to see why we are seen as industry leaders.</p>
</div>
<span class="btn abs" style="left:585px;top:930px">Know More</span>

<section class="products-bg" role="img" aria-label="Photograph of a steel door set into a brick building"></section>
<h2 class="section-title heading" style="top:1140px;color:var(--ink)">Our Products</h2>
<div class="section-rule abs" style="left:550px;top:1183px"></div>
<div class="products-copy">
  <h3>Fire Exist Doors</h3>
  <p>Tolvane steel fire exit doors are designed and manufactured to the same high standards as the multi-locking personnel door.</p>
  <p style="margin-top:8px">Tolvane steel fire exit doors can be supplied to meet the specific requirements of your project.</p>
  <ul><li>Anti-vandal steel cabins</li><li>Modular buildings</li><li>Steel framed buildings</li><li>General building projects</li></ul>
  <a>Read More</a>
</div>
<div class="product-frame" role="img" aria-label="Photograph of a blue steel fire exit door in a corridor with extinguishers"></div>
<div class="dots"><i></i><i class="on"></i><i></i></div>

<section class="contact-band"></section>
<div class="contact-photo" role="img" aria-label="Photograph of a customer service advisor wearing a headset"></div>
<h2 class="section-title heading contact-title">Contact US</h2>
<div class="section-rule abs" style="left:550px;top:1733px;background:var(--yellow)"></div>
<p class="contact-lead">Let's start the conversation! If you have a question and are interested in speaking to someone from Tolvane Eng. Ltd.</p>
<div class="contact-actions">
  <span class="ghost"><svg width="12" height="12" viewBox="0 0 12 12"><path d="M2 1c1 4 4 7 9 9l1-2-2.5-1.5-1 .8C6.8 6.5 5.5 5.2 4.7 3.5l.8-1L4 0z" fill="#f3d700"/></svg>+44 (0)1632 960 300</span>
  <span class="or">OR</span>
  <span class="ghost">Online Order Form</span>
</div>

<h2 class="section-title heading reviews-title">Happy Customer Reviews</h2>
<div class="section-rule abs" style="left:550px;top:1945px"></div>
<div class="arrow-btn" style="left:141px;top:2020px;background:#999"><svg width="8" height="10" viewBox="0 0 8 10"><path d="M6 1L2 5l4 4" stroke="#fff" stroke-width="2" fill="none"/></svg></div>
<div class="arrow-btn" style="left:1035px;top:2020px;background:var(--teal)"><svg width="8" height="10" viewBox="0 0 8 10"><path d="M2 1l4 4-4 4" stroke="#fff" stroke-width="2" fill="none"/></svg></div>
<div class="avatar" style="left:280px;top:2000px;width:58px;height:64px" role="img" aria-label="Customer portrait"></div>
<div class="avatar" style="left:420px;top:2000px;width:58px;height:64px" role="img" aria-label="Customer portrait"></div>
<div class="avatar" style="left:548px;top:1982px;width:92px;height:102px;background:var(--teal-light)"></div>
<div class="avatar" style="left:556px;top:1991px;width:76px;height:84px" role="img" aria-label="Featured customer portrait"></div>
<div class="avatar" style="left:712px;top:2000px;width:58px;height:64px" role="img" aria-label="Customer portrait"></div>
<div class="avatar" style="left:858px;top:2000px;width:58px;height:64px" role="img" aria-label="Customer portrait"></div>
<p class="quote">"Lorem Ipsum is simply dummy text of the printing and typesetting industry. Lorem Ipsum has been the industry's standard dummy text ever since the 1500s, when an unknown printer took a galley of type and scrambled it to make a type specimen book."</p>
<div class="quote-mark">”</div>
<p class="reviewer">Daniel Hartley</p>

<section class="latest-bg" role="img" aria-label="Photograph of a modern apartment building"></section>
<h2 class="section-title heading latest-title">Our Latest Products</h2>
<div class="section-rule abs" style="left:550px;top:2412px"></div>
<article class="latest-card">
  <div class="latest-copy">
    <h3>Anti-Vandal Shroud</h3>
    <p>Tolvane Engineering's anti-vandal shroud has been designed to offer increased security protection for the standard 10-point locking personnel door.</p>
    <p><strong>Construction &amp; Features</strong></p>
    <p>3mm stainless steel internal and external shrouds protect the euro-cylinder enabling it to resist a physical attack.</p>
    <p>Please contact us for more information with regards to the Tolvane Anti-Vandal Shroud.</p>
    <span class="btn" style="margin-top:4px">Know More</span>
  </div>
  <div class="latest-image" role="img" aria-label="Photograph of a steel door handle with multi-point lock"></div>
</article>

<h2 class="section-title heading downloads-title">Download Our Brochures</h2>
<div class="section-rule abs" style="left:550px;top:2922px"></div>
<div class="brochure" style="left:143px;width:204px"><svg width="34" height="38" viewBox="0 0 34 38"><path d="M4 1h18l8 8v28H4z" fill="none" stroke="#4d8789" stroke-width="2"/><path d="M17 13v14M11 21l6 6 6-6" stroke="#4d8789" stroke-width="2.5" fill="none"/></svg>10-Point Locking Steel<br>Personnel Doors Brochure</div>
<div class="brochure" style="left:377px;width:203px"><svg width="34" height="38" viewBox="0 0 34 38"><path d="M4 1h18l8 8v28H4z" fill="none" stroke="#4d8789" stroke-width="2"/><path d="M17 13v14M11 21l6 6 6-6" stroke="#4d8789" stroke-width="2.5" fill="none"/></svg>Steel Fire Exit<br>Doors Brochure</div>
<div class="brochure" style="left:611px;width:215px"><svg width="34" height="38" viewBox="0 0 34 38"><path d="M4 1h18l8 8v28H4z" fill="none" stroke="#4d8789" stroke-width="2"/><path d="M17 13v14M11 21l6 6 6-6" stroke="#4d8789" stroke-width="2.5" fill="none"/></svg>Anti-Vandal Steel Shutters &amp;<br>Glazing Units Brochure</div>
<div class="brochure" style="left:855px;width:203px"><svg width="34" height="38" viewBox="0 0 34 38"><path d="M4 1h18l8 8v28H4z" fill="none" stroke="#4d8789" stroke-width="2"/><path d="M17 13v14M11 21l6 6 6-6" stroke="#4d8789" stroke-width="2.5" fill="none"/></svg>Vision Panels</div>

<footer>
  <div class="footer-bg" role="img" aria-label="Photograph of a city skyline at dusk"></div>
  <div class="footer-actions">
    <span class="ghost"><svg width="12" height="12" viewBox="0 0 12 12"><path d="M2 1c1 4 4 7 9 9l1-2-2.5-1.5-1 .8C6.8 6.5 5.5 5.2 4.7 3.5l.8-1L4 0z" fill="#f3d700"/></svg>+44 (0)1632 960 300</span>
    <span class="or">OR</span>
    <span class="ghost">Online Order Form</span>
  </div>
  <div class="footer-col" style="left:143px"><h4>Quick Links</h4><div class="bar"></div>
    <ul><li>Home</li><li>About</li><li>Product &amp; Accessories</li><li>Delivery &amp; Lead Times</li><li>Downloads</li><li>Contact</li></ul></div>
  <div class="footer-col" style="left:305px"><h4>Products</h4><div class="bar"></div>
    <ul><li>Personnel Doors</li><li>Fire Exit Doors</li><li>Blank Doors</li><li>Acoustic Doors</li><li style="line-height:15px;margin-top:5px">Anti-vandal Steel Shutters &amp;<br>Glazing Units</li></ul></div>
  <div class="footer-col" style="left:472px"><h4>Contact Us</h4><div class="bar"></div>
    <div class="address"><svg width="14" height="18" viewBox="0 0 14 18"><path d="M7 17S1 10 1 6.5a6 6 0 0 1 12 0C13 10 7 17 7 17z" fill="none" stroke="#f3d700" stroke-width="1.6"/><circle cx="7" cy="6.5" r="2" fill="#f3d700"/></svg><span>Tolvane Engineering Ltd.<br>Harlow Hill, Mill Lane<br>Ashwick, Kelbridge UK KB4 7QT</span></div>
    <div class="address"><svg width="14" height="14" viewBox="0 0 12 12"><path d="M2 1c1 4 4 7 9 9l1-2-2.5-1.5-1 .8C6.8 6.5 5.5 5.2 4.7 3.5l.8-1L4 0z" fill="#f3d700"/></svg><span>+44 (0) 1632 960300<br>+44 (0) 1632 960400 ( Fax)</span></div>
    <div class="address"><svg width="16" height="12" viewBox="0 0 16 12"><rect x="1" y="1" width="14" height="10" fill="none" stroke="#f3d700" stroke-width="1.5"/><path d="M1 1l7 6 7-6" stroke="#f3d700" stroke-width="1.5" fill="none"/></svg><span>info@tolvadoors.com</span></div>
  </div>
  <div class="display-stand" role="img" aria-label="Product brochure display stand"></div>
  <div class="footer-col" style="left:830px"><h4>Quick Inquiry</h4><div class="bar"></div>
    <div class="field">Name:</div><div class="field">Email:</div><div class="field" style="height:44px">Message:</div>
    <span class="submit">SUBMIT</span></div>
  <p class="copyright">Copyright © 2016 Tolvane Engineering Ltd . All Rights Reserved.</p>
  <div class="socials"><i></i><i></i><i></i><i></i></div>
</footer>

</body>
</html>
```